deceased estate clean ups brochures

we would like a brochure to reresent our business we already have new web site and want to do DL A4 brochure to give out to promote our business we already have logo www.larkmore.com.au is where you can get all info needed

Target Market(s)

families with loved ones that have past away
people done sizing or needing to decluter

Colors
cadf82
33b8a4
886aae
33a6d7

```html
<!DOCTYPE html>
<html lang="en">
<head>
<meta charset="utf-8">
<title>Larkmore – Deceased Estate Clean Ups Brochure</title>
<link href="https://fonts.googleapis.com/css2?family=Open+Sans:wght@400;600;700;800&display=swap" rel="stylesheet">
<style>
:root{
  --green-dark:#3a7f35;
  --green:#4c9a3f;
  --green-light:#8cc63f;
  --lime:#c5e07a;
  --grey-text:#5a5a5a;
  --grey-soft:#e6e6e6;
  --paper:#ffffff;
  --backdrop:#ececec;
}
*{margin:0;padding:0;box-sizing:border-box}
html,body{width:1200px;height:962px;overflow:hidden;background:var(--backdrop);font-family:"Open Sans",Arial,sans-serif}
.spread{position:absolute;left:275px;width:650px;height:460px;background:var(--paper);box-shadow:0 2px 8px rgba(0,0,0,.15);overflow:hidden}
.spread--inside{top:14px}
.spread--outside{top:488px}
.spread-art{position:absolute;inset:0;width:650px;height:460px}
.fold{position:absolute;top:0;bottom:0;width:1px;background:rgba(0,0,0,.06)}
.block{position:absolute}
.heading{font-weight:700;font-size:13px;letter-spacing:.5px;text-transform:uppercase}
.heading--light{color:#fff}
.rule{height:1.5px;background:#fff;margin-top:4px;width:120px}
.body-light{color:#fff;font-size:7.4px;line-height:1.45;text-align:justify}
.body-light p+p{margin-top:7px}
.why-title{font-weight:800;font-size:17px;line-height:1;color:var(--green);text-align:right;text-transform:uppercase}
.feature{position:absolute;left:232px;width:190px;display:flex;gap:8px}
.feature-icon{flex:0 0 18px;height:18px;border-radius:50%;background:var(--green);display:flex;align-items:center;justify-content:center}
.feature-name{font-size:7.4px;font-weight:700;color:var(--green);text-transform:uppercase}
.feature-text{font-size:5.8px;line-height:1.35;color:var(--grey-text)}
.service{position:absolute;left:444px;width:196px;display:flex;gap:7px}
.service-tick{flex:0 0 15px;height:15px}
.service-name{font-size:7.2px;font-weight:700;color:var(--green);text-transform:uppercase;line-height:1.15}
.service-text{font-size:5.4px;line-height:1.35;color:var(--grey-text);margin-top:2px}
.call-badge{position:absolute;left:286px;top:164px;width:78px;height:78px;border-radius:50%;background:var(--green);border:3px solid #fff;color:#fff;text-align:center;padding-top:13px}
.call-badge svg{display:block;margin:0 auto 3px}
.call-label{font-size:6.2px;font-weight:700;line-height:1.2}
.call-number{font-size:6.4px;font-weight:700;margin-top:3px;white-space:nowrap}
.steps{color:#fff;font-size:7.4px;line-height:1.4}
.steps li{list-style:none;margin-bottom:6px}
.step-label{display:block}
.contact-bubble{position:absolute;left:270px;top:8px;width:140px;height:140px;border-radius:50%;background:var(--grey-soft);border:4px solid #fff;box-shadow:0 0 0 3px var(--green-light);text-align:center;padding-top:20px}
.contact-title{font-size:15px;font-weight:800;color:var(--green);text-transform:uppercase}
.contact-sub{font-size:10px;font-weight:700;color:var(--green);margin-top:1px}
.contact-note{font-size:7.4px;line-height:1.35;color:var(--grey-text);margin:8px auto 0;width:96px;border-top:1px solid var(--green);padding-top:5px}
.brand{display:flex;align-items:center;gap:6px;font-weight:700;color:#555;letter-spacing:1px;text-transform:uppercase}
.brand-dot{border-radius:50%;background:var(--green-light)}
.contact-list{position:absolute;left:244px;top:290px;list-style:none;font-size:7.4px;color:var(--grey-text)}
.contact-list li{display:flex;align-items:center;gap:7px;margin-bottom:9px}
.contact-icon{width:12px;height:12px;flex:0 0 12px}
.cover-band{position:absolute;left:433px;top:318px;width:217px;height:44px;background:var(--green);color:#fff;text-align:center;font-size:10.5px;font-weight:700;line-height:1.2;padding-top:9px;text-transform:uppercase}
.cover-url{position:absolute;left:433px;top:376px;width:217px;text-align:center;font-size:8.6px;font-weight:700;color:var(--green-dark)}
</style>
</head>
<body>

<section class="spread spread--inside" aria-label="Brochure inside spread">
  <svg class="spread-art" viewBox="0 0 650 460" aria-hidden="true">
    <defs>
      <linearGradient id="greenFill" x1="0" y1="0" x2="1" y2="1">
        <stop offset="0" stop-color="#3a7f35"/><stop offset="1" stop-color="#5aa843"/>
      </linearGradient>
      <linearGradient id="limeFill" x1="0" y1="0" x2="1" y2="0">
        <stop offset="0" stop-color="#8cc63f"/><stop offset="1" stop-color="#c5e07a"/>
      </linearGradient>
    </defs>
    <path d="M0 0H217V255C160 290 80 300 0 345Z" fill="url(#greenFill)"/>
    <path d="M0 345C80 300 160 290 217 255V268C160 300 80 312 0 358Z" fill="url(#limeFill)"/>
    <path d="M217 0H433V120C380 165 300 175 217 240Z" fill="url(#greenFill)"/>
    <path d="M217 240C300 175 380 165 433 120V132C380 178 300 188 217 252Z" fill="url(#limeFill)"/>
    <path d="M433 0H650V108C580 122 500 132 433 170Z" fill="url(#greenFill)"/>
    <path d="M433 170C500 132 580 122 650 108V120C580 134 500 144 433 182Z" fill="url(#limeFill)"/>
    <path d="M0 460V440C200 438 420 438 650 424V460Z" fill="url(#limeFill)"/>
    <path d="M0 447C200 445 420 445 650 431V437C420 451 200 452 0 453Z" fill="#3a7f35"/>
  </svg>
  <div class="fold" style="left:217px"></div>
  <div class="fold" style="left:433px"></div>

  <div class="block" style="left:14px;top:16px;width:190px">
    <h2 class="heading heading--light">About Us</h2>
    <div class="rule"></div>
    <div class="body-light" style="margin-top:10px">
      <p>At Larkmore our goal is to ease your worries and help you with your journey in preparing your house for rental or resale. Whether it is a move to another residence or the difficult task with dealing with the grief when a loved one passes away, Larkmore can help with the preparation of the property for sale.</p>
      <p>Larkmore will come in, remove unwanted items and dispose of all rubbish, do cosmetic repairs if required and leave the property in a spotless state.</p>
    </div>
  </div>
  <svg class="block" style="left:14px;top:312px" width="128" height="128" viewBox="0 0 128 128" role="img" aria-label="Photo: tradesman holding a clipboard">
    <defs><linearGradient id="photoA" x1="0" y1="0" x2="0" y2="1"><stop offset="0" stop-color="#c9c9c9"/><stop offset="1" stop-color="#8f8f8f"/></linearGradient></defs>
    <circle cx="64" cy="64" r="62" fill="#fff" stroke="#8cc63f" stroke-width="3"/>
    <circle cx="64" cy="64" r="55" fill="url(#photoA)"/>
  </svg>

  <svg class="block" style="left:245px;top:16px" width="160" height="160" viewBox="0 0 160 160" role="img" aria-label="Photo: elderly couple sitting together outside their home">
    <defs><linearGradient id="photoB" x1="0" y1="0" x2="0" y2="1"><stop offset="0" stop-color="#d4d4d4"/><stop offset="1" stop-color="#8f8f8f"/></linearGradient></defs>
    <circle cx="80" cy="80" r="78" fill="#fff"/>
    <circle cx="80" cy="80" r="71" fill="url(#photoB)"/>
  </svg>
  <div class="call-badge">
    <svg width="11" height="11" viewBox="0 0 24 24" aria-hidden="true"><path d="M6.6 10.8a15 15 0 0 0 6.6 6.6l2.2-2.2a1 1 0 0 1 1-.25 11.4 11.4 0 0 0 3.6.6 1 1 0 0 1 1 1V20a1 1 0 0 1-1 1A17 17 0 0 1 3 4a1 1 0 0 1 1-1h3.5a1 1 0 0 1 1 1 11.4 11.4 0 0 0 .6 3.6 1 1 0 0 1-.25 1Z" fill="#fff"/></svg>
    <div class="call-label">CALL US<br>TODAY</div>
    <div class="call-number">0400 318 624</div>
  </div>

  <div class="block" style="left:300px;top:250px;width:120px">
    <h2 class="why-title">Why<br>Choose Us</h2>
  </div>
  <div class="feature" style="top:298px">
    <span class="feature-icon"><svg width="10" height="10" viewBox="0 0 24 24" aria-hidden="true"><circle cx="12" cy="12" r="7" fill="none" stroke="#fff" stroke-width="3"/></svg></span>
    <div><div class="feature-name">Quality</div><div class="feature-text">Our goal is to enhance your property and achieve the results you are looking for.</div></div>
  </div>
  <div class="feature" style="top:328px">
    <span class="feature-icon"><svg width="10" height="10" viewBox="0 0 24 24" aria-hidden="true"><path d="M4 11h4v10H4zM10 21V11l4-8c2 0 3 1 2.5 3L16 9h5l-2 12z" fill="#fff"/></svg></span>
    <div><div class="feature-name">Pride</div><div class="feature-text">We take pride in our family approach and care we bring to your loved ones belongings.</div></div>
  </div>
  <div class="feature" style="top:358px">
    <span class="feature-icon"><svg width="10" height="10" viewBox="0 0 24 24" aria-hidden="true"><path d="M3 21V9h4v12zM10 21V5h4v16zM17 21V12h4v9z" fill="#fff"/></svg></span>
    <div><div class="feature-name">Professionalism</div><div class="feature-text">We keep a professional approach to every job ensuring all agreed tasks are completed and accounted for.</div></div>
  </div>
  <div class="feature" style="top:388px">
    <span class="feature-icon"><svg width="10" height="10" viewBox="0 0 24 24" aria-hidden="true"><path d="M12 2a7 7 0 0 0-7 7c0 5 7 13 7 13s7-8 7-13a7 7 0 0 0-7-7zm0 9.5A2.5 2.5 0 1 1 12 6.5a2.5 2.5 0 0 1 0 5z" fill="#fff"/></svg></span>
    <div><div class="feature-name">Areas Serviced</div><div class="feature-text">Specialising in Melbourne CBD and suburbs. If you're not sure we service your area, give us a call.</div></div>
  </div>

  <div class="block" style="left:447px;top:16px;width:190px">
    <h2 class="heading heading--light">Our Services</h2>
    <div class="rule"></div>
    <p class="body-light" style="margin-top:8px">Our trained and reliable staff repair any house and carry out landscaping in preparation for renting or resale of the property in a timely &amp; professional manner.</p>
  </div>

  <div class="service" style="top:190px">
    <svg class="service-tick" viewBox="0 0 24 24" aria-hidden="true"><circle cx="12" cy="12" r="10" fill="none" stroke="#8cc63f" stroke-width="2.5"/><path d="M7 12l4 4 7-8" fill="none" stroke="#4c9a3f" stroke-width="3"/></svg>
    <div><div class="service-name">Senior / Aged Care<br>Relocations &amp; Down Sizing</div><div class="service-text">Decluttering &amp; sorting your belongings, packing, moving and unpacking into your new home, removing all unwanted items.</div></div>
  </div>
  <div class="service" style="top:227px">
    <svg class="service-tick" viewBox="0 0 24 24" aria-hidden="true"><circle cx="12" cy="12" r="10" fill="none" stroke="#8cc63f" stroke-width="2.5"/><path d="M7 12l4 4 7-8" fill="none" stroke="#4c9a3f" stroke-width="3"/></svg>
    <div><div class="service-name">Deceased<br>Estates</div><div class="service-text">Losing a loved one and finalising their estate can be difficult and traumatic for families. Let our professional team help.</div></div>
  </div>
  <div class="service" style="top:264px">
    <svg class="service-tick" viewBox="0 0 24 24" aria-hidden="true"><circle cx="12" cy="12" r="10" fill="none" stroke="#8cc63f" stroke-width="2.5"/><path d="M7 12l4 4 7-8" fill="none" stroke="#4c9a3f" stroke-width="3"/></svg>
    <div><div class="service-name">Cleaning<br>Service</div><div class="service-text">We provide a cleaning service for a house sale or rental preparation. Let us make these decisions hassle free and within budget.</div></div>
  </div>
  <div class="service" style="top:301px">
    <svg class="service-tick" viewBox="0 0 24 24" aria-hidden="true"><circle cx="12" cy="12" r="10" fill="none" stroke="#8cc63f" stroke-width="2.5"/><path d="M7 12l4 4 7-8" fill="none" stroke="#4c9a3f" stroke-width="3"/></svg>
    <div><div class="service-name">Cosmetic Repairs and<br>House Maintenance</div><div class="service-text">We are experienced in cosmetic repairs and house renovations and can help you achieve the best return on the property.</div></div>
  </div>
  <div class="service" style="top:338px">
    <svg class="service-tick" viewBox="0 0 24 24" aria-hidden="true"><circle cx="12" cy="12" r="10" fill="none" stroke="#8cc63f" stroke-width="2.5"/><path d="M7 12l4 4 7-8" fill="none" stroke="#4c9a3f" stroke-width="3"/></svg>
    <div><div class="service-name">Preparation for<br>Rental or Sale</div><div class="service-text">We can do cosmetic renovations, clean and declutter your entire home, leaving it market ready to sell, rent or move into.</div></div>
  </div>
  <div class="service" style="top:375px">
    <svg class="service-tick" viewBox="0 0 24 24" aria-hidden="true"><circle cx="12" cy="12" r="10" fill="none" stroke="#8cc63f" stroke-width="2.5"/><path d="M7 12l4 4 7-8" fill="none" stroke="#4c9a3f" stroke-width="3"/></svg>
    <div><div class="service-name">Garden<br>Makeovers</div><div class="service-text">We run a successful landscaping business, The Fernvale Group, offering a full service in landscaping and construction.</div></div>
  </div>
</section>

<section class="spread spread--outside" aria-label="Brochure outside spread">
  <svg class="spread-art" viewBox="0 0 650 460" aria-hidden="true">
    <defs>
      <linearGradient id="greenFill2" x1="0" y1="0" x2="1" y2="1">
        <stop offset="0" stop-color="#3a7f35"/><stop offset="1" stop-color="#5aa843"/>
      </linearGradient>
      <linearGradient id="limeFill2" x1="0" y1="0" x2="1" y2="0">
        <stop offset="0" stop-color="#8cc63f"/><stop offset="1" stop-color="#c5e07a"/>
      </linearGradient>
    </defs>
    <path d="M0 0H217V290C190 330 160 360 120 380C80 400 40 420 0 460Z" fill="url(#greenFill2)"/>
    <path d="M217 290C190 330 160 360 120 380C80 400 40 420 0 460H14C50 428 90 408 130 388C170 368 198 336 217 306Z" fill="url(#limeFill2)"/>
    <path d="M217 0H300C260 40 240 120 217 170Z" fill="url(#greenFill2)"/>
    <path d="M217 460H433V395C380 430 300 450 217 455Z" fill="url(#greenFill2)"/>
    <path d="M217 455C300 450 380 430 433 395V385C380 420 300 440 217 446Z" fill="url(#limeFill2)"/>
    <path d="M433 0H650V170C590 210 500 215 433 190Z" fill="url(#greenFill2)"/>
    <path d="M433 190C500 215 590 210 650 170V182C590 222 500 227 433 202Z" fill="url(#limeFill2)"/>
    <rect x="433" y="312" width="217" height="3" fill="#8cc63f"/>
    <rect x="433" y="365" width="217" height="3" fill="#8cc63f"/>
    <rect x="433" y="448" width="217" height="12" fill="url(#limeFill2)"/>
  </svg>
  <div class="fold" style="left:217px"></div>
  <div class="fold" style="left:433px"></div>

  <div class="block" style="left:14px;top:18px;width:192px">
    <h2 class="heading heading--light">Our 5 Step Process</h2>
    <div class="rule"></div>
    <ol class="steps" style="margin-top:10px">
      <li><span class="step-label">STEP 1:</span>We start with a consultation at the property, understanding our client's needs, requests and priorities. Create a plan of what needs to be done in each step of your move.</li>
      <li><span class="step-label">STEP 2:</span>Pre-sale decluttering and sorting of items. Unwanted items to be sold, given to friends, family or charity.</li>
      <li><span class="step-label">STEP 3:</span>Cleaning the property (inside and outside) prior to sale or rent.</li>
      <li><span class="step-label">STEP 4:</span>Organising and arranging transport of your possessions.</li>
      <li><span class="step-label">STEP 5:</span>Storage or unpacking your possessions and setting up as per your instructions.</li>
    </ol>
  </div>
  <svg class="block" style="left:66px;top:336px" width="112" height="112" viewBox="0 0 112 112" role="img" aria-label="Photo: worker on a ladder repairing a house exterior">
    <defs><linearGradient id="photoC" x1="0" y1="0" x2="0" y2="1"><stop offset="0" stop-color="#d0d0d0"/><stop offset="1" stop-color="#7d7d7d"/></linearGradient></defs>
    <circle cx="56" cy="56" r="54" fill="#fff" stroke="#3a7f35" stroke-width="3"/>
    <circle cx="56" cy="56" r="48" fill="url(#photoC)"/>
  </svg>

  <div class="contact-bubble">
    <div class="contact-title">Contact</div>
    <div class="contact-sub">Larkmore Today!</div>
    <p class="contact-note">A company that cares solely about your best interest and the care for the estate of your loved one.</p>
  </div>
  <div class="block brand" style="left:268px;top:212px;font-size:14px">
    <span class="brand-dot" style="width:14px;height:14px"></span>Larkmore
  </div>
  <ul class="contact-list">
    <li><svg class="contact-icon" viewBox="0 0 24 24" aria-hidden="true"><circle cx="12" cy="12" r="11" fill="#4c9a3f"/><path d="M8.5 10.5a9 9 0 0 0 5 5l1.3-1.3 2.7 1v2.3c-6 .5-11-4.5-10.5-10.5h2.3l1 2.7z" fill="#fff"/></svg>0400 318 624</li>
    <li><svg class="contact-icon" viewBox="0 0 24 24" aria-hidden="true"><circle cx="12" cy="12" r="11" fill="#4c9a3f"/><circle cx="12" cy="12" r="6" fill="none" stroke="#fff" stroke-width="1.6"/><path d="M6 12h12M12 6v12" stroke="#fff" stroke-width="1.4"/></svg>www.larkmore.com.au</li>
    <li><svg class="contact-icon" viewBox="0 0 24 24" aria-hidden="true"><circle cx="12" cy="12" r="11" fill="#4c9a3f"/><rect x="6" y="8" width="12" height="8" fill="none" stroke="#fff" stroke-width="1.5"/><path d="M6 8l6 5 6-5" fill="none" stroke="#fff" stroke-width="1.5"/></svg>info@larkmore.com.au</li>
    <li><svg class="contact-icon" viewBox="0 0 24 24" aria-hidden="true"><circle cx="12" cy="12" r="11" fill="#4c9a3f"/><path d="M12 5a4.5 4.5 0 0 0-4.5 4.5C7.5 13 12 19 12 19s4.5-6 4.5-9.5A4.5 4.5 0 0 0 12 5z" fill="#fff"/></svg>PO Box 88, Kingsford 3010</li>
  </ul>

  <svg class="block" style="left:451px;top:20px" width="180" height="180" viewBox="0 0 180 180" role="img" aria-label="Photo: cleaners wiping a glass table and mopping a living room floor">
    <defs><linearGradient id="photoD" x1="0" y1="0" x2="1" y2="1"><stop offset="0" stop-color="#efe9df"/><stop offset="1" stop-color="#a8a39a"/></linearGradient></defs>
    <circle cx="90" cy="90" r="88" fill="#fff" stroke="#8cc63f" stroke-width="3"/>
    <circle cx="90" cy="90" r="80" fill="url(#photoD)"/>
  </svg>
  <div class="block brand" style="left:470px;top:262px;font-size:19px">
    <span class="brand-dot" style="width:18px;height:18px"></span>Larkmore
  </div>
  <div class="cover-band">Deceased Estate<br>Clean Ups</div>
  <div class="cover-url">www.larkmore.com.au</div>
</section>

</body>
</html>
```